Food Menu for Entertainment Show Venue

Using the attached food menu we will need these food, the prices and dietary notes with a table.

Colour theme is pink, baby pink and hot pink. I have attached the drinks menu so you have the vibe of drinks.

Will be on an A5 or A4 venue menu. Happy to have an A3 that folds out also. Open to all ideas.

```html
<!DOCTYPE html>
<html lang="en">
<head>
<meta charset="utf-8">
<title>Food Menu – The Coral Heron Showclub</title>
<link rel="stylesheet" href="https://fonts.googleapis.com/css2?family=Anton&family=Josefin+Sans:wght@700&display=swap">
<style>
  :root{
    --plum:#5a1f3a;
    --badge:#9c4a72;
    --white:#ffffff;
    --band:#d484a8;
    --pink-hot:#d565a0;
    --pink-mid:#dc93c0;
    --pink-baby:#e9bccb;
    --body:'Josefin Sans', Arial, sans-serif;
    --display:'Anton', Impact, sans-serif;
  }
  *{margin:0;padding:0;box-sizing:border-box}
  html,body{width:848px;height:1200px;overflow:hidden}
  .menu-card{position:relative;width:848px;height:1200px;overflow:hidden;font-family:var(--body);color:var(--plum)}
  .backdrop{position:absolute;inset:0;background:
      radial-gradient(ellipse 60% 70% at 40% 55%, var(--pink-hot) 0%, transparent 70%),
      linear-gradient(180deg, var(--pink-mid) 0%, var(--pink-baby) 100%)}
  .price-band{position:absolute;left:695px;top:0;width:153px;height:1200px;background:var(--band)}
  .side-title{position:absolute;left:0;top:0;width:100px;height:430px}
  .side-title span{position:absolute;left:50px;top:215px;transform:translate(-50%,-50%) rotate(-90deg);
      font-family:var(--body);font-weight:700;font-size:140px;line-height:1;color:var(--white);letter-spacing:-2px;white-space:nowrap}
  .brand{position:absolute;left:170px;top:120px;width:400px;text-align:center;color:var(--white);font-weight:700;letter-spacing:3px}
  .brand .brand-small{font-size:24px;display:block}
  .brand .brand-big{font-size:60px;line-height:1.1;display:block;letter-spacing:4px}
  .brand .brand-sub{font-size:34px;display:block}
  .rule{position:absolute;left:110px;top:352px;width:563px;height:6px;background:var(--white)}
  .item{position:absolute;left:111px}
  .item-name{font-size:22px;letter-spacing:2.2px;line-height:1;display:flex;align-items:center;gap:10px;white-space:nowrap}
  .item-note{font-size:13px;letter-spacing:1px;margin-top:4px}
  .badge{display:inline-flex;align-items:center;justify-content:center;width:36px;height:36px;border-radius:50%;
      background:var(--badge);color:var(--white);font-size:14px;letter-spacing:0;margin-left:14px}
  .badge + .badge{margin-left:-6px}
  .price{position:absolute;left:714px;font-size:22px;letter-spacing:2px;white-space:pre}
  .burger-box{position:absolute;left:93px;top:818px;width:560px;height:220px;border:5px solid var(--white)}
  .burger{position:absolute;left:20px;right:20px;display:flex;justify-content:space-between;
      font-family:var(--display);font-size:27px;letter-spacing:.5px;color:var(--plum)}
  .legend{position:absolute;top:1086px;display:flex;flex-direction:column;align-items:center;width:110px}
  .legend-label{font-size:12px;letter-spacing:1px;margin-bottom:8px}
  .legend .badge{width:48px;height:48px;font-size:20px;margin:0}
</style>
</head>
<body>
<main class="menu-card">
  <div class="backdrop" role="img" aria-label="Pink, baby pink and hot pink rays converging towards the bottom"></div>
  <div class="price-band"></div>

  <h1 class="side-title"><span>menu</span></h1>

  <header class="brand">
    <span class="brand-small">THE</span>
    <span class="brand-big">CORAL HERON</span>
    <span class="brand-sub">SHOWCLUB</span>
  </header>

  <div class="rule"></div>

  <div class="item" style="top:404px"><div class="item-name">MOZZARELLA STICKS <span class="badge">V</span></div><div class="item-note">TOMATO RELISH</div></div>
  <div class="price" style="top:404px">$  9.00</div>

  <div class="item" style="top:475px"><div class="item-name">CRISPY FRIES <span class="badge">GF</span><span class="badge">VG</span></div></div>
  <div class="price" style="top:475px">$  9.00</div>

  <div class="item" style="top:525px"><div class="item-name">VEGETARIAN SPRING ROLLS <span class="badge">VG</span></div><div class="item-note">SWEET CHILLI SAUCE</div></div>
  <div class="price" style="top:525px">$  12.00</div>

  <div class="item" style="top:594px"><div class="item-name">KARRAGE CHIKEN BITES <span class="badge">V</span></div><div class="item-note">CHIPLOTE MAYO</div></div>
  <div class="price" style="top:594px">$  16.00</div>

  <div class="item" style="top:668px"><div class="item-name">CAULIFLOWER POPCORN <span class="badge">V</span></div><div class="item-note">SWEET CHILLI SAUCE</div></div>
  <div class="price" style="top:668px">$  14.00</div>

  <div class="item" style="top:740px"><div class="item-name">TRUFFLE AND PORCINI ARANCINI <span class="badge">GF</span><span class="badge">V</span></div><div class="item-note">TOMATO RELISH</div></div>
  <div class="price" style="top:740px">$  18.00</div>

  <section class="burger-box">
    <div class="burger" style="top:20px"><span>CLASSIC ANGUS BEEF BURGER</span><span>$ 18</span></div>
    <div class="burger" style="top:90px"><span>CRISPY CHICKEN BURGER</span><span>$ 18</span></div>
    <div class="burger" style="top:160px"><span>CLASSIC PLANT BURGER</span><span>$ 18</span></div>
  </section>

  <div class="legend" style="left:170px"><span class="legend-label">VEGAN</span><span class="badge">VG</span></div>
  <div class="legend" style="left:282px"><span class="legend-label">VEGETARIAN</span><span class="badge">V</span></div>
  <div class="legend" style="left:394px"><span class="legend-label">GLUTEN FREE</span><span class="badge">GF</span></div>
</main>
</body>
</html>
```